Home Improvement Company in need of a "Banner & Billboard Design"

I'm Looking for a Banner design 4X6 With Company Logo, Phone Number, website, Credentials and services.. I picture a charcoal/matte background i also want to look like a house shape design i will upload the sample...

I'm looking for a Billboard design to target homeowners who need Roofing Services. I need logo, number, website, KLN, Credentials and a catchy title. i will like to use the same colors for branding

Target Market(s)

Homeowners, Investors,

Industry/Entity Type

Home Improvement

Font styles to use
Decorative

Colors
00a990
5c5c5c
333333

Requirements
Must have
• All Credentials, Phone number, website, logo, logo colors, services, Eye Catchy, Direct Message, Friendly feeling,
• (555) 319 - 4826
• Roofing Gutters Painting Pressure Washing Exterior Design
Nice to have
• A catchy title, A direct message to a homeowner looking for home improvement services. noticeable
Should not have
• not Busy, no

```html
<!DOCTYPE html>
<html lang="en">
<head>
<meta charset="utf-8">
<title>Crestline Home Exteriors – Banner</title>
<link href="https://fonts.googleapis.com/css2?family=Ubuntu:wght@500;700&family=Fira+Sans+Condensed:wght@600&display=swap" rel="stylesheet">
<style>
  :root {
    --teal: #00a990;
    --teal-band: #1f9683;
    --charcoal: #333333;
    --charcoal-deep: #2b2b2b;
    --slate: #5c5c5c;
    --band-gray: #4a4a4a;
    --icon-gray: #2f2f2f;
    --white: #ffffff;
    --badge-red: #c8322c;
    --badge-navy: #1c2f6b;
    --page: #ffffff;
  }
  * { margin: 0; padding: 0; box-sizing: border-box; }
  html, body {
    width: 1044px;
    height: 1200px;
    overflow: hidden;
    background: var(--page);
  }
  .banner {
    position: absolute;
    left: 22px;
    top: 266px;
    width: 1000px;
    height: 667px;
    overflow: hidden;
    background: radial-gradient(ellipse at 60% 40%, var(--charcoal) 0%, var(--charcoal-deep) 100%);
    box-shadow: 0 3px 8px rgba(0,0,0,0.35);
  }
  .banner-shapes {
    position: absolute;
    inset: 0;
  }
  .brand {
    position: absolute;
    left: 58px;
    top: 100px;
    display: flex;
    align-items: flex-start;
    gap: 14px;
  }
  .brand-mark {
    width: 26px;
    height: 26px;
    margin-top: 12px;
    background: var(--teal);
  }
  .brand-name {
    font-family: "Ubuntu", sans-serif;
    font-weight: 700;
    color: var(--teal);
    font-size: 44px;
    line-height: 1.05;
    letter-spacing: 0.5px;
  }
  .phone {
    position: absolute;
    left: 56px;
    top: 326px;
    font-family: "Ubuntu", sans-serif;
    font-weight: 700;
    font-size: 66px;
    color: var(--white);
    letter-spacing: 1px;
  }
  .website {
    position: absolute;
    left: 62px;
    top: 444px;
    font-family: "Ubuntu", sans-serif;
    font-weight: 700;
    font-size: 36px;
    color: var(--white);
  }
  .services {
    position: absolute;
    left: 658px;
    top: 92px;
    list-style: none;
    font-family: "Fira Sans Condensed", sans-serif;
    font-weight: 600;
    font-size: 33px;
    line-height: 52px;
    color: var(--white);
  }
  .services li {
    position: relative;
    padding-left: 34px;
  }
  .services li::before {
    content: "";
    position: absolute;
    left: 0;
    top: 19px;
    width: 15px;
    height: 13px;
    background: var(--teal);
  }
  .services li.continued::before { display: none; }
  .badge-cert {
    position: absolute;
    left: 662px;
    top: 462px;
    width: 186px;
    height: 70px;
  }
  .badge-kln {
    position: absolute;
    left: 870px;
    top: 402px;
    width: 78px;
    height: 130px;
    border-radius: 6px;
    background: var(--badge-navy);
    border: 3px solid #d9dde8;
  }
</style>
</head>
<body>
  <section class="banner">
    <svg class="banner-shapes" viewBox="0 0 1000 667" width="1000" height="667" aria-hidden="true">
      <polygon class="contact-band" points="0,580 520,580 495,657 0,657" fill="var(--band-gray)"/>
      <polygon class="accent-band" points="575,540 1000,540 1000,667 512,667" fill="var(--teal-band)"/>
      <g class="contact-icons" fill="none" stroke="var(--icon-gray)" stroke-width="4" stroke-linecap="round" stroke-linejoin="round">
        <path d="M115 604 c-4 8 2 22 14 32 c10 8 20 10 26 6 l5 -6 l-10 -9 l-6 5 c-5 -2 -12 -9 -14 -14 l5 -6 l-9 -10 z"/>
        <circle cx="195" cy="621" r="18"/>
        <path d="M177 621 h36 M195 603 c-9 10 -9 26 0 36 M195 603 c9 10 9 26 0 36"/>
        <rect x="236" y="608" width="40" height="27" rx="2"/>
        <path d="M236 610 l20 15 l20 -15"/>
      </g>
    </svg>

    <div class="brand">
      <span class="brand-mark"></span>
      <span class="brand-name">Crestline<br>Home Exteriors</span>
    </div>

    <div class="phone">(555) 319 - 4826</div>
    <div class="website">www.CrestlineExteriors.com</div>

    <ul class="services">
      <li>Roofing Gutters</li>
      <li>Painting Pressure</li>
      <li>Washing Exterior</li>
      <li class="continued">Design</li>
    </ul>

    <svg class="badge-cert" viewBox="0 0 186 70" role="img" aria-label="Roofing certification badge">
      <polygon points="30,28 93,2 156,28" fill="var(--icon-gray)"/>
      <rect x="0" y="28" width="186" height="42" rx="3" fill="var(--badge-red)"/>
    </svg>
    <div class="badge-kln" role="img" aria-label="KLN accreditation badge"></div>
  </section>
</body>
</html>
```